Velmora Company needs a Business Card Design

We just opened our business recently and we need a business card design. Our basic product are clothes and accessories. We would like to see designs that use bright colors like pink, light blue and purple. In addition to that kindly include also our address in the business card which our main office is located in Los Angeles, California.
The final design should communicate that we have affordable price yet high quality brand.

Target Market(s)

young and middle age women

Industry/Entity Type

Business

Contact Information for Business Card

Velmora Apparel and Accessories 3847 North Hollis St. Los Angeles California
Tel: 424-583-6094

Logo Text

Velmora's Apparel and Accessories

Font styles to use
Serif

Requirements
Must have
• there should be a graphic of a sexy lady wearing an elegant dress at the upper left corner of the business card.

```html
<!DOCTYPE html>
<html lang="en">
<head>
<meta charset="utf-8">
<title>Velmora Apparel and Accessories – Business Card</title>
<link rel="stylesheet" href="https://fonts.googleapis.com/css2?family=Source+Sans+3:wght@400;700&family=Didact+Gothic&display=swap">
<style>
  :root {
    --page-bg: #ffffff;
    --card-pink: #f5989a;
    --card-ink: #ffffff;
  }
  * { margin: 0; padding: 0; box-sizing: border-box; }
  html, body {
    width: 1200px;
    height: 1000px;
    overflow: hidden;
    background: var(--page-bg);
  }
  .canvas {
    position: relative;
    width: 1200px;
    height: 1000px;
  }
  .business-card {
    position: absolute;
    left: 262px;
    top: 266px;
    width: 678px;
    height: 387px;
    background: var(--card-pink);
    color: var(--card-ink);
    text-align: center;
  }
  .brand {
    position: absolute;
    left: 0;
    right: 0;
    top: 76px;
  }
  .brand-name {
    font-family: "Source Sans 3", sans-serif;
    font-weight: 700;
    font-size: 58px;
    line-height: 58px;
    letter-spacing: 0.5px;
  }
  .brand-tagline {
    font-family: "Source Sans 3", sans-serif;
    font-weight: 400;
    font-size: 21px;
    line-height: 24px;
    margin-top: 0;
  }
  .contact {
    position: absolute;
    left: 0;
    right: 0;
    top: 238px;
    font-family: "Didact Gothic", sans-serif;
    font-style: normal;
    font-size: 24px;
    line-height: 38px;
    letter-spacing: 1.2px;
  }
</style>
</head>
<body>
  <main class="canvas">
    <section class="business-card" aria-label="Velmora business card">
      <header class="brand">
        <div class="brand-name">VELMORA</div>
        <div class="brand-tagline">Apparel and Accessories</div>
      </header>
      <address class="contact">
        <div class="contact-street">3847 North Hollis St.</div>
        <div class="contact-city">Los Angeles California</div>
        <div class="contact-phone">Tel: 424-583-6094</div>
      </address>
    </section>
  </main>
</body>
</html>
```